Poster Design Project

Poster with modern feeling to be displayed in office. The text that needs to be included in this poster is below:

Rules
1. If it’s not in writing it doesn’t exist.
2. No such thing as 'off the record.'
3. Do not hold a private conversation in a public place.
4. Don’t believe any number that ends in zero.
5. Never turn down an opportunity to eat or go to the bathroom.
6. Don’t spend any of your own money. Don’t even admit you own a credit card. Don’t spend money that is not yours.
7. Not always a 'right' or 'wrong' answer - 'It depends.'
8. In a campaign, someone has to be in charge – campaigns are a place to foster democracy, not practice it.
9. Assume nothing.
10. If you make a mistake, fix it before analyzing. Bad news doesn’t age well.

Industry/Entity Type

Credit Card

Requirements
Must have
• Rules
7. Not always a “right” or “wrong” answer - 'It depends.' 
9. Assume nothing.

```html
<!DOCTYPE html>
<html lang="en">
<head>
<meta charset="utf-8">
<title>Rules Poster</title>
<link rel="stylesheet" href="https://fonts.googleapis.com/css2?family=Roboto+Condensed:wght@700&display=swap">
<style>
  :root {
    --page-bg: #ffffff;
    --poster-edge: #fdf18f;
    --poster-mid: #fef7b8;
    --poster-center: #fffde8;
    --ink: #141414;
  }
  html, body {
    margin: 0;
    padding: 0;
    width: 1200px;
    height: 900px;
    overflow: hidden;
    background: var(--page-bg);
  }
  .canvas {
    position: relative;
    width: 1200px;
    height: 900px;
  }
  .poster {
    position: absolute;
    left: 310px;
    top: 3px;
    width: 580px;
    height: 897px;
    background: radial-gradient(ellipse 60% 55% at 50% 48%, var(--poster-center) 0%, var(--poster-mid) 55%, var(--poster-edge) 100%);
    font-family: "Roboto Condensed", "Arial Narrow", sans-serif;
    font-weight: 700;
    color: var(--ink);
  }
  .poster-title {
    position: absolute;
    left: 0;
    right: 0;
    top: 40px;
    margin: 0;
    text-align: center;
    font-size: 66px;
    line-height: 76px;
    letter-spacing: -0.5px;
    padding-left: 16px;
  }
  .title-rule {
    position: absolute;
    left: 60px;
    top: 127px;
    width: 458px;
    height: 16px;
  }
  .rules-list {
    position: absolute;
    left: 88px;
    top: 170px;
    width: 440px;
    margin: 0;
    padding: 0;
    list-style: none;
    font-size: 20.5px;
    line-height: 28px;
  }
  .rule {
    position: relative;
    padding-left: 40px;
    margin-bottom: 14.5px;
  }
  .rule-number {
    position: absolute;
    left: 0;
    width: 34px;
    text-align: right;
  }
</style>
</head>
<body>
<div class="canvas">
  <main class="poster">
    <h1 class="poster-title">RULES</h1>
    <svg class="title-rule" viewBox="0 0 458 16" aria-hidden="true">
      <rect x="0" y="1" width="458" height="4" fill="#141414"/>
      <rect x="0" y="10" width="458" height="4" fill="#141414"/>
    </svg>
    <ol class="rules-list">
      <li class="rule"><span class="rule-number">1.</span>If it’s not in writing it doesn’t exist.</li>
      <li class="rule"><span class="rule-number">2.</span>No such thing as 'off the record.'</li>
      <li class="rule"><span class="rule-number">3.</span>Do not hold a private conversation in<br>a public place.</li>
      <li class="rule"><span class="rule-number">4.</span>Don’t believe any number that ends<br>in zero.</li>
      <li class="rule"><span class="rule-number">5.</span>Never turn down an opportunity to<br>eat or go to the bathroom.</li>
      <li class="rule"><span class="rule-number">6.</span>Don’t spend any of your own money.<br>Don’t even admit you own a credit card.<br>Don’t spend money that is not yours.</li>
      <li class="rule"><span class="rule-number">7.</span>Not always a 'right' or 'wrong'<br>answer - 'It depends.'</li>
      <li class="rule"><span class="rule-number">8.</span>In a campaign, someone has to be in<br>charge – campaigns are a place to<br>foster democracy, not practice it.</li>
      <li class="rule"><span class="rule-number">9.</span>Assume nothing.</li>
      <li class="rule"><span class="rule-number">10.</span>If you make a mistake, fix it before<br>analyzing. Bad news doesn’t age well.</li>
    </ol>
  </main>
</div>
</body>
</html>
```